Upscale business cards needed for family business

We need professional business cards created for several family members. We are a family business holding company. We would like these relatively simple and straightforward, but also with a unique element to set them apart. Probably stick with neutral and simple colors - white, grey etc. We need space for the traditional elements, including name, title, address, email/phone number. And we will be creating several from this template so it needs to be template that is easy to switch information in and out of.

Industry/Entity Type

Business

Contact Information for Business Card

Please include the attached Marwood Capital logo.

Requirements
Must have
• The attached Marwood Capital logo.

```html
<!DOCTYPE html>
<html lang="en">
<head>
<meta charset="utf-8">
<title>Marwood Capital – Business Card</title>
<link rel="stylesheet" href="https://fonts.googleapis.com/css2?family=Libre+Baskerville&family=Raleway:wght@400;500&display=swap">
<style>
  :root {
    --backdrop: #5d6670;
    --card-white: #ffffff;
    --card-black: #000000;
    --gold: #e0ac1f;
    --text-light: #ffffff;
    --brand-ink: #2a2a2a;
  }
  html, body {
    margin: 0;
    width: 1200px;
    height: 675px;
    overflow: hidden;
    background: var(--backdrop);
  }
  .card {
    position: absolute;
    left: 75px;
    top: 37px;
    width: 1050px;
    height: 600px;
    background: var(--card-white);
    overflow: hidden;
  }
  .card__shapes {
    position: absolute;
    inset: 0;
  }
  .brand {
    position: absolute;
    left: 250px;
    top: 150px;
    display: flex;
    align-items: center;
    gap: 14px;
    font-family: "Libre Baskerville", serif;
    font-size: 30px;
    letter-spacing: 2px;
    text-transform: uppercase;
    color: var(--brand-ink);
  }
  .brand__dot {
    width: 14px;
    height: 14px;
    border-radius: 50%;
    background: var(--gold);
  }
  .contact {
    position: absolute;
    left: 470px;
    top: 300px;
    width: 540px;
    font-family: "Raleway", sans-serif;
    color: var(--text-light);
  }
  .contact__name {
    margin: 0;
    font-family: "Libre Baskerville", serif;
    font-size: 38px;
    font-weight: 400;
    color: var(--gold);
  }
  .contact__title {
    margin: 2px 0 22px 50px;
    font-size: 22px;
  }
  .contact__line {
    margin: 0 0 6px;
    font-size: 23px;
  }
  .contact__rule {
    height: 1px;
    margin: 14px 0 14px;
    background: var(--gold);
  }
  .contact__address {
    margin: 0;
    font-size: 23px;
  }
</style>
</head>
<body>
  <div class="card">
    <svg class="card__shapes" viewBox="0 0 1050 600" width="1050" height="600" aria-hidden="true">
      <path class="card__accent-curve" d="M30 505 Q420 170 1050 112" fill="none" stroke="#e0ac1f" stroke-width="9"/>
      <path class="card__dark-field" d="M0 560 Q430 200 1050 140 L1050 600 L0 600 Z" fill="#000000"/>
    </svg>

    <div class="brand">
      <span class="brand__dot"></span>
      <span class="brand__name">Marwood Capital</span>
    </div>

    <div class="contact">
      <h1 class="contact__name">John Doe</h1>
      <p class="contact__title">Director</p>
      <p class="contact__line">+01 123 456 7890</p>
      <p class="contact__line">john@marwoodcapital.com</p>
      <div class="contact__rule"></div>
      <p class="contact__address">123 Dummy Street, Dummy City, Dummy Country</p>
    </div>
  </div>
</body>
</html>
```